This is a a hair cutting class for hair stylist

Flyer with dates time place couple of pics with hair styles. Need it web media compatible. Design needs to be for a 2 sided flier. This flier need to stand out but be clean and professional. Mainly use the top info in the word doc for text in the flier.

done done done done done done done done done done done done done done done done done done done

Target Market(s)

Professional stylist and Cosmetology students

Industry/Entity Type

Hair And Beauty

Font styles to use
Sans Serif

Colors
33a6d7

Requirements
Must have
• Clear text and can use for Instagram and Facebook . must be designed to be used on both sides of a flyer 4x6 .
Nice to have
• picture cleanup if flaws are notices.
Should not have
• dark colors

```html
<!DOCTYPE html>
<html lang="en">
<head>
<meta charset="utf-8">
<title>Short Hair Cuts Workshop Flyer – Front and Back</title>
<link rel="stylesheet" href="https://fonts.googleapis.com/css2?family=Archivo+Black&family=Oswald:wght@400;500;600;700&family=Raleway:wght@300&family=Playfair+Display:wght@400;700&display=swap">
<style>
  :root {
    --page: #ececec;
    --pink: #e6007e;
    --pink-soft: #f6b9da;
    --pink-wash: #fbe3f0;
    --purple: #8a2a8c;
    --plum: #6a1f70;
    --blue: #33a6d7;
    --blue-soft: #bfe4f4;
    --navy: #0f3d63;
    --ink: #1a1a1a;
    --grey: #6b6b6b;
    --white: #ffffff;
  }
  * { box-sizing: border-box; margin: 0; padding: 0; }
  html, body { width: 1200px; height: 844px; overflow: hidden; background: var(--page); }
  .canvas { position: relative; width: 1200px; height: 844px; }

  .flyer {
    position: absolute; top: 41px; width: 532px; height: 762px;
    background: var(--white); overflow: hidden;
    box-shadow: 0 2px 8px rgba(0,0,0,.15);
    font-family: "Oswald", sans-serif;
  }
  .flyer--front { left: 44px; background: linear-gradient(180deg, var(--pink-wash) 0%, #fdf2f8 60%, var(--white) 85%); }
  .flyer--back { left: 624px; background: linear-gradient(180deg, var(--blue) 0%, #5fbbe2 40%, #e8f5fb 72%, var(--white) 85%); }

  .photo { position: absolute; }
  .flyer--front .photo { left: 0; top: 20px; width: 340px; height: 470px;
    background: radial-gradient(ellipse at 45% 40%, #b0653d 0%, #d89a8a 35%, #f0bcd6 65%, rgba(246,185,218,0) 80%); }
  .flyer--back .photo { right: 0; top: 30px; width: 300px; height: 520px;
    background: radial-gradient(ellipse at 55% 38%, #101a2e 0%, #3a4a66 30%, #7fb9d6 60%, rgba(95,187,226,0) 80%); }

  .brand { position: absolute; top: 24px; font-family: "Archivo Black", sans-serif; font-size: 33px; line-height: 36px; letter-spacing: -0.5px; }
  .flyer--front .brand { right: 40px; color: var(--purple); text-align: right; }
  .flyer--back .brand { left: 32px; color: var(--white); }

  .role-tag { position: absolute; top: 60px; height: 14px; padding: 0 6px; font-family: "Raleway", sans-serif; font-size: 12px; line-height: 14px; letter-spacing: .5px; }
  .flyer--front .role-tag { right: 40px; width: 152px; background: var(--purple); color: var(--white); border: 1px solid var(--white); }
  .flyer--back .role-tag { left: 32px; width: 152px; background: var(--blue); color: var(--white); border: 1px solid var(--white); }

  .headline { position: absolute; top: 76px; font-weight: 500; font-size: 52px; line-height: 45px; text-transform: uppercase; }
  .flyer--front .headline { right: 40px; text-align: right; }
  .flyer--back .headline { left: 32px; }
  .headline span { display: block; }
  .flyer--front .hl-1, .flyer--front .hl-2, .flyer--front .hl-3 { color: var(--pink); }
  .flyer--front .hl-4 { color: var(--purple); }
  .flyer--back .hl-1, .flyer--back .hl-2 { color: var(--white); }
  .flyer--back .hl-3, .flyer--back .hl-4 { color: var(--navy); }

  .workshop { position: absolute; top: 260px; width: 214px; height: 64px; background: var(--white); text-align: center; border-left: 3px solid var(--ink); box-shadow: 0 2px 4px rgba(0,0,0,.2); }
  .flyer--front .workshop { right: 40px; }
  .flyer--back .workshop { left: 32px; }
  .workshop-lead { font-family: "Raleway", sans-serif; font-weight: 300; font-size: 34px; line-height: 38px; color: var(--ink); }
  .workshop-sub { font-size: 15.5px; line-height: 20px; font-weight: 500; color: var(--ink); text-transform: uppercase; }

  .badge { position: absolute; border-radius: 50%; text-align: center; overflow: hidden; border: 4px solid var(--white); box-shadow: 0 3px 8px rgba(0,0,0,.25); }

  .date { width: 224px; height: 224px; }
  .flyer--front .date { left: 270px; top: 324px; background: radial-gradient(circle at 40% 30%, var(--white) 0%, var(--pink-soft) 70%, #ea7fbb 100%); }
  .flyer--back .date { left: 36px; top: 324px; background: radial-gradient(circle at 40% 30%, var(--white) 0%, var(--blue-soft) 70%, #7cc7e7 100%); }
  .date-day { position: absolute; left: 40px; top: 32px; font-family: "Playfair Display", serif; font-size: 15px; color: var(--white); letter-spacing: .5px; }
  .date-month { position: absolute; left: 18px; top: 42px; font-family: "Playfair Display", serif; font-size: 40px; line-height: 44px; }
  .date-time { position: absolute; left: 48px; top: 86px; font-family: "Playfair Display", serif; font-size: 24px; line-height: 26px; }
  .date-year { position: absolute; left: 40px; top: 110px; font-family: "Playfair Display", serif; font-weight: 700; font-size: 30px; line-height: 32px; }
  .date-num { position: absolute; left: 126px; top: 0; font-family: "Playfair Display", serif; font-size: 150px; line-height: 160px; }
  .flyer--front .date-month, .flyer--front .date-year, .flyer--front .date-num { color: var(--purple); }
  .flyer--front .date-time { color: var(--pink); }
  .flyer--back .date-month, .flyer--back .date-year, .flyer--back .date-num { color: var(--navy); }
  .flyer--back .date-time { color: var(--blue); }
  .venue { position: absolute; left: 0; right: 0; top: 144px; height: 80px; padding-top: 3px; color: var(--white); line-height: 15px; }
  .flyer--front .venue { background: var(--pink); }
  .flyer--back .venue { background: var(--blue); }
  .venue-name { font-size: 16px; font-weight: 600; line-height: 18px; }
  .venue-line { font-size: 12.5px; font-weight: 400; }
  .flyer--front .venue-line { color: var(--plum); }
  .flyer--back .venue-line { color: var(--navy); }
  .venue-tel { font-size: 12.5px; font-weight: 500; }

  .price { width: 120px; height: 120px; padding-top: 26px; text-transform: uppercase; }
  .flyer--front .price { background: radial-gradient(circle at 40% 30%, var(--white) 0%, var(--pink-soft) 60%, #ec6fb3 100%); }
  .flyer--back .price { background: radial-gradient(circle at 40% 30%, #7dcbeb 0%, var(--blue) 60%, #1b7fb0 100%); }
  .price-label { font-size: 14px; line-height: 16px; font-weight: 500; }
  .price-label small { font-size: 11px; }
  .price-amount { font-size: 38px; line-height: 40px; font-weight: 500; }
  .price-amount sup { font-size: 16px; vertical-align: 18px; }
  .flyer--front .price-label { color: var(--purple); }
  .flyer--front .price-amount { color: var(--white); text-shadow: 0 0 2px var(--pink); }
  .flyer--back .price-label, .flyer--back .price-amount { color: var(--white); }
  .price--only { padding-top: 28px; }

  .book { width: 128px; height: 128px; padding-top: 30px; text-transform: uppercase; }
  .flyer--front .book { left: 222px; top: 532px; background: radial-gradient(circle at 40% 30%, #f04aa4 0%, var(--pink) 70%, #b8006a 100%); color: var(--white); }
  .flyer--back .book { left: 174px; top: 528px; background: var(--white); color: var(--ink); border-color: var(--navy); }
  .book-kicker { font-size: 13px; line-height: 16px; font-weight: 500; }
  .book-main { font-size: 44px; line-height: 44px; font-weight: 600; }
  .book-tail { font-size: 17px; line-height: 18px; font-weight: 500; }

  .overview { position: absolute; top: 536px; width: 190px; }
  .flyer--front .overview { left: 50px; }
  .flyer--back .overview { right: 48px; text-align: right; }
  .overview-title { font-family: "Playfair Display", serif; font-size: 17px; color: var(--grey); line-height: 22px; }
  .overview-list { list-style: none; }
  .overview-item { position: relative; font-size: 12.5px; line-height: 13px; text-transform: uppercase; margin-top: 6px; }
  .overview-item--head { font-size: 14px; font-weight: 700; text-transform: none; line-height: 16px; margin-top: 5px; }
  .flyer--front .overview-item { padding-left: 18px; color: var(--plum); }
  .flyer--front .overview-item--head { color: var(--pink); }
  .flyer--back .overview-item { color: var(--blue); }
  .flyer--back .overview-item--head { color: var(--navy); }
  .overview-icon { position: absolute; left: 0; top: 1px; width: 12px; height: 12px; }

  .booking { position: absolute; top: 676px; font-family: "Raleway", sans-serif; font-weight: 300; font-size: 19px; color: var(--ink); }
  .flyer--front .booking { left: 194px; }
  .flyer--back .booking { left: 34px; }
  .phones { position: absolute; top: 698px; font-family: "Oswald", sans-serif; font-weight: 700; font-size: 24px; letter-spacing: .2px; }
  .flyer--front .phones { left: 138px; color: var(--pink); }
  .flyer--back .phones { left: 34px; color: var(--blue); }
  .phones-or { font-family: "Raleway", sans-serif; font-weight: 300; font-size: 16px; margin: 0 6px; }
</style>
</head>
<body>
<div class="canvas">

  <!-- Front side -->
  <section class="flyer flyer--front">
    <div class="photo" role="img" aria-label="Photo of a stylist with a short copper curled haircut, seen in profile"></div>

    <div class="brand">MARISA VALE</div>
    <div class="role-tag">MASTER STYLIST</div>
    <h1 class="headline">
      <span class="hl-1">Short</span><span class="hl-2">Hair Cuts</span><span class="hl-3">Shear</span><span class="hl-4">Perfection</span>
    </h1>
    <div class="workshop">
      <div class="workshop-lead">Hands on</div>
      <div class="workshop-sub">Short Haircutting Workshop</div>
    </div>

    <div class="badge price" style="left:148px;top:408px;">
      <div class="price-label">Observation<br><small>and</small> Hands on</div>
      <div class="price-amount"><sup>$</sup>275<sup>.00</sup></div>
    </div>

    <div class="badge date">
      <div class="date-day">SUNDAY</div>
      <div class="date-month">APRIL</div>
      <div class="date-time">9-5PM</div>
      <div class="date-year">2017</div>
      <div class="date-num">2</div>
      <div class="venue">
        <div class="venue-name">THE LUNETTE SALON</div>
        <div class="venue-line">418 CEDAR LANE, WESTBROOK</div>
        <div class="venue-line">OREGON 97000</div>
        <div class="venue-tel">TEL: 5550101234</div>
      </div>
    </div>

    <div class="badge book">
      <div class="book-kicker">Limited Space!</div>
      <div class="book-main">Book</div>
      <div class="book-tail">Yours Today</div>
    </div>

    <div class="badge price price--only" style="left:372px;top:548px;">
      <div class="price-label">Observation<br>Only</div>
      <div class="price-amount"><sup>$</sup>175<sup>.00</sup></div>
    </div>

    <div class="overview">
      <div class="overview-title">Class Overview</div>
      <ul class="overview-list">
        <li class="overview-item overview-item--head"><svg class="overview-icon" viewBox="0 0 12 12"><circle cx="6" cy="6" r="5" fill="none" stroke="#e6007e" stroke-width="1"/><path d="M5 4l2.5 2L5 8z" fill="#e6007e"/></svg>Observation Only</li>
        <li class="overview-item"><svg class="overview-icon" viewBox="0 0 12 12"><rect x="1" y="2" width="9" height="9" fill="none" stroke="#8a2a8c"/><path d="M3 6l2 2.5L11 1" fill="none" stroke="#8a2a8c" stroke-width="1.6"/></svg>Hair Consultation</li>
        <li class="overview-item"><svg class="overview-icon" viewBox="0 0 12 12"><rect x="1" y="2" width="9" height="9" fill="none" stroke="#8a2a8c"/><path d="M3 6l2 2.5L11 1" fill="none" stroke="#8a2a8c" stroke-width="1.6"/></svg>Step-by-step haircutting demonstration</li>
        <li class="overview-item overview-item--head"><svg class="overview-icon" viewBox="0 0 12 12"><circle cx="6" cy="6" r="5" fill="none" stroke="#e6007e" stroke-width="1"/><path d="M5 4l2.5 2L5 8z" fill="#e6007e"/></svg>Hands-on Haircutting</li>
        <li class="overview-item"><svg class="overview-icon" viewBox="0 0 12 12"><rect x="1" y="2" width="9" height="9" fill="none" stroke="#8a2a8c"/><path d="M3 6l2 2.5L11 1" fill="none" stroke="#8a2a8c" stroke-width="1.6"/></svg>Practice short haircutting</li>
      </ul>
    </div>

    <div class="booking">Booking &amp; Inquiries, please call</div>
    <div class="phones">555 210 4471<span class="phones-or">OR</span>555 380 9126</div>
  </section>

  <!-- Back side -->
  <section class="flyer flyer--back">
    <div class="photo" role="img" aria-label="Photo of a stylist with a short black curled haircut, seen from behind"></div>

    <div class="brand">MARISA VALE</div>
    <div class="role-tag">MASTER STYLIST</div>
    <h1 class="headline">
      <span class="hl-1">Short</span><span class="hl-2">Hair Cuts</span><span class="hl-3">Shear</span><span class="hl-4">Perfection</span>
    </h1>
    <div class="workshop">
      <div class="workshop-lead">Hands on</div>
      <div class="workshop-sub">Short Haircutting Workshop</div>
    </div>

    <div class="badge date">
      <div class="date-day">SUNDAY</div>
      <div class="date-month">APRIL</div>
      <div class="date-time">9-5PM</div>
      <div class="date-year">2017</div>
      <div class="date-num">2</div>
      <div class="venue">
        <div class="venue-name">THE LUNETTE SALON</div>
        <div class="venue-line">418 CEDAR LANE, WESTBROOK</div>
        <div class="venue-line">OREGON 97000</div>
        <div class="venue-tel">TEL: 5550101234</div>
      </div>
    </div>

    <div class="badge price" style="left:256px;top:402px;">
      <div class="price-label">Observation<br><small>and</small> Hands on</div>
      <div class="price-amount"><sup>$</sup>275<sup>.00</sup></div>
    </div>

    <div class="badge price price--only" style="left:36px;top:544px;">
      <div class="price-label">Observation<br>Only</div>
      <div class="price-amount"><sup>$</sup>175<sup>.00</sup></div>
    </div>

    <div class="badge book">
      <div class="book-kicker">Limited Offer!</div>
      <div class="book-main">Book</div>
      <div class="book-tail">Yours Today</div>
    </div>

    <div class="overview">
      <div class="overview-title">Class Overview</div>
      <ul class="overview-list">
        <li class="overview-item overview-item--head">Observation Only</li>
        <li class="overview-item">Hair Consultation</li>
        <li class="overview-item">Step-by-step haircutting<br>demonstration</li>
        <li class="overview-item overview-item--head">Hands-on Haircutting</li>
        <li class="overview-item">Practice short<br>haircutting</li>
      </ul>
    </div>

    <div class="booking">Booking &amp; Inquiries, please call</div>
    <div class="phones">555 210 4471<span class="phones-or">OR</span>555 380 9126</div>
  </section>

</div>
</body>
</html>
```